【依頼の目的/概要】
電子書籍(pavlo)の表紙デザインをお願いします

【画像サイズ】
*RVSより抜粋
表紙ファイルの理想的な寸法は2,560×1,600ピクセルです。
注:画像の寸法は1,000×625ピクセル以上であることが必要です
画像の最大の寸法は10,000×10,000ピクセルです

【タイトル】
朝の庭で見つけた小さな灯りの話

サブキャッチ
~来場者2倍、満足度9割の老舗書店を育てた5つの習慣

【著者】
ミドリノタネ工房代表
組織進化コンサルタント
柳瀬 公平

【本の内容】
とても勤勉で勉強家の開業歯科医のみなさんが
がんばってもなかなか成果の出づらい分野、
「チーム創り」について。

まず互いを人として大事にすることで
スタッフが自然に結束し、
「ここで働けてよかった」
と思うようになる。
楽しいから自主的創造的に動くようになる。
すると成果の質も高くなる。
そうなるまでのステップを紹介。

著者はレポートを出す型のコンサルではなく、
現場に入り込んでゲーム性の高い体験型研修や
一人一人の話を聴いて言葉にならない本音を通訳することなどが得意。
愛と遊び心をもってプログラムを提供し伴走するので
笑顔が絶えることがない。

*参考資料として原稿を添付します

【デザイン要望】
特にイメージにこだわりはありませんので
自由な発想でのデザインご応募を楽しみにしています。

*次点、次々点の方への参加報酬を設定いたしました。

*その他、必要な情報がありましたらお問い合わせください。

スマホでpavloを見るとき、小さなアイコンが並ぶ中で最も目に留まるデザインで、
一目で重要なワードも目に入るデザインだったので採用させていただきました。

次点の二つについても同様の基準でしたが
色使いやフォントサイズなどを調整して、
もっとパッと目に入るものでしたら順序が変わったかもしれません。

特に、チームがテーマなので人の写真+見やすいデザインが両方だったらよりよかったかなと思います

皆さま、一所懸命やっていただいてありがとうございました。
こんなにもたくさんの方にご提案いただけてとてもうれしいです。
お礼を出せるのは3作品ですが
皆様にお礼を改めて申し上げたいと思います。

電子書籍の売れ行きにとても大事な表紙づくりのご協力、本当にありがとうございました。

```html
<!DOCTYPE html>
<html lang="ja">
<head>
<meta charset="UTF-8">
<title>朝の庭で見つけた小さな灯りの話</title>
<link rel="stylesheet" href="https://fonts.googleapis.com/css2?family=Noto+Sans+JP:wght@500;700;900&display=swap">
<style>
  :root {
    --ink: #111111;
    --accent: #d7262b;
    --paper: #ffffff;
    --photo-light: #f6f3f1;
    --photo-mid: #e9dedb;
    --photo-deep: #cfc4c2;
  }
  * { margin: 0; padding: 0; box-sizing: border-box; }
  html, body { width: 750px; height: 1200px; overflow: hidden; background: var(--paper); }
  .cover {
    position: relative;
    width: 750px;
    height: 1200px;
    background: var(--paper);
    font-family: "Noto Sans JP", sans-serif;
    color: var(--ink);
    overflow: hidden;
  }
  .cover-photo {
    position: absolute;
    left: 0; top: 740px;
    width: 750px; height: 460px;
    background:
      radial-gradient(ellipse at 50% 70%, var(--photo-mid) 0%, rgba(233,222,219,0) 65%),
      linear-gradient(180deg, var(--paper) 0%, var(--photo-light) 30%, var(--photo-mid) 75%, var(--photo-deep) 100%);
  }
  .vcol {
    position: absolute;
    writing-mode: vertical-rl;
    text-orientation: upright;
    line-height: 1;
    white-space: nowrap;
  }
  .title-line {
    top: 22px;
    font-size: 85px;
    font-weight: 900;
    letter-spacing: 0;
  }
  .title-line--1 { left: 616px; }
  .title-line--2 { left: 476px; }
  .title-line--3 { left: 320px; color: var(--accent); }
  .divider {
    position: absolute;
    left: 278px; top: 40px;
    width: 4px; height: 600px;
    background: var(--accent);
  }
  .subtitle-line {
    top: 30px;
    font-size: 55px;
    font-weight: 900;
    letter-spacing: 2px;
  }
  .subtitle-line--1 { left: 184px; }
  .subtitle-line--2 { left: 47px; }
  .subtitle-line .num { color: var(--accent); }
  .emphasis {
    color: var(--accent);
    text-emphasis: filled dot var(--accent);
    text-emphasis-position: left;
  }
  .author {
    position: absolute;
    right: 20px; top: 655px;
    text-align: right;
    font-weight: 700;
    font-size: 23px;
    line-height: 1.5;
  }
  .author-name { font-size: 26px; margin-top: 6px; letter-spacing: 4px; }
  .steps-badge {
    position: absolute;
    left: 405px; top: 795px;
    width: 195px; height: 185px;
    border: 5px solid var(--accent);
    border-radius: 22px;
    background: var(--paper);
    color: var(--accent);
    font-weight: 900;
    font-size: 44px;
    line-height: 1.25;
    display: flex;
    flex-direction: column;
    align-items: center;
    justify-content: center;
    text-align: center;
  }
</style>
</head>
<body>
  <div class="cover">
    <div class="cover-photo" role="img" aria-label="歯の模型の上で働く小さな人形たちのチームの写真"></div>

    <h1 class="book-title">
      <span class="vcol title-line title-line--1">朝の庭で</span>
      <span class="vcol title-line title-line--2">見つけた</span>
      <span class="vcol title-line title-line--3">小さな灯りの話</span>
    </h1>

    <div class="divider"></div>

    <p class="subtitle">
      <span class="vcol subtitle-line subtitle-line--1">来場者<span class="num">2</span>倍満足度<span class="num">9</span>割の</span>
      <span class="vcol subtitle-line subtitle-line--2"><span class="emphasis">老舗書店</span>を育てた</span>
    </p>

    <div class="author">
      <p>ミドリノタネ工房代表</p>
      <p>組織進化コンサルタント</p>
      <p class="author-name">柳瀬 公平</p>
    </div>

    <div class="steps-badge">
      <span>5つの</span>
      <span>習慣</span>
    </div>
  </div>
</body>
</html>
```